Banner for construction site to identify developer

we need a 4 foot by 8 foot banner to hang on the fence of a residential townhome development in Phoenix, Arizona that identifies Tolvane Holdings as the company behind the development/project. Also needs to include the logo, phone number, and web address. Would like to stick with the blue colors provided in the attached logo. The blues should stay the same but the letters in the logo can change to another color if necessary. Feel free to use "Tolvane Holdings" in place of "Tolvane Holdings Group". Looking for use of colors/design to take up space so banner is not just text with a logo.

Target Market(s)

drive by traffic looking at the site

Industry/Entity Type

Real Estate

Colors
0054AA
0677BA
7BADD7
CADEEF
E8F1F8

Requirements
Must have
• company name, phone number and web address

```html
<!DOCTYPE html>
<html lang="en">
<head>
<meta charset="utf-8">
<title>Tolvane Holdings – Site Banner</title>
<link rel="stylesheet" href="https://fonts.googleapis.com/css2?family=Fira+Sans:wght@400;600&family=Fira+Sans+Condensed:wght@400&display=swap">
<style>
  :root {
    --blue-deep: #0054AA;
    --blue-mid: #0677BA;
    --blue-soft: #7BADD7;
    --blue-pale: #CADEEF;
    --blue-mist: #E8F1F8;
    --ink: #1c1c1e;
    --white: #ffffff;
    --stage: #d4d5d6;
  }
  html, body {
    margin: 0;
    width: 1200px;
    height: 910px;
    overflow: hidden;
    background: var(--stage);
  }
  .banner {
    position: absolute;
    left: 0;
    top: 155px;
    width: 1200px;
    height: 600px;
    overflow: hidden;
  }
  .banner-art {
    position: absolute;
    inset: 0;
  }
  .brand {
    position: absolute;
    left: 62px;
    top: 218px;
    display: flex;
    align-items: center;
    gap: 26px;
  }
  .brand-square {
    width: 92px;
    height: 92px;
    background: var(--blue-mid);
  }
  .brand-name {
    font-family: "Fira Sans", sans-serif;
    font-weight: 600;
    font-size: 104px;
    letter-spacing: -2px;
    line-height: 1;
    color: var(--ink);
    white-space: nowrap;
  }
  .contact {
    position: absolute;
    left: 64px;
    top: 428px;
    font-family: "Fira Sans Condensed", sans-serif;
    color: var(--white);
    font-size: 46px;
    line-height: 1.32;
  }
  .address {
    position: absolute;
    right: 58px;
    top: 464px;
    text-align: right;
    font-family: "Fira Sans Condensed", sans-serif;
    color: var(--white);
    font-size: 26px;
    line-height: 1.4;
  }
</style>
</head>
<body>
  <div class="banner">
    <svg class="banner-art" viewBox="0 0 1200 600" width="1200" height="600" aria-hidden="false">
      <defs>
        <linearGradient id="field" x1="0" y1="0" x2="1" y2="1">
          <stop offset="0" stop-color="#E8F1F8"/>
          <stop offset="1" stop-color="#CADEEF"/>
        </linearGradient>
        <linearGradient id="skyline" x1="0" y1="0" x2="0" y2="1">
          <stop offset="0" stop-color="#CADEEF" stop-opacity="0"/>
          <stop offset="1" stop-color="#7BADD7" stop-opacity="0.28"/>
        </linearGradient>
        <linearGradient id="band" x1="0" y1="0" x2="1" y2="0">
          <stop offset="0" stop-color="#0677BA"/>
          <stop offset="1" stop-color="#0054AA"/>
        </linearGradient>
      </defs>
      <rect class="field" width="1200" height="600" fill="url(#field)"/>
      <rect class="skyline-backdrop" x="240" y="90" width="960" height="340" fill="url(#skyline)" role="img" aria-label="Faint line drawing of townhomes and apartment buildings"/>
      <polygon class="band-top" points="230,0 1200,0 1200,100" fill="url(#band)"/>
      <polygon class="band-bottom" points="0,372 1200,462 1200,600 0,600" fill="url(#band)"/>
    </svg>

    <div class="brand">
      <div class="brand-square"></div>
      <div class="brand-name">Tolvane Holdings</div>
    </div>

    <div class="contact">
      <div class="phone">(480) 555-0147</div>
      <div class="web">tolvaneholdings.com</div>
    </div>

    <div class="address">
      <div>4120 N. 12th Ave Suite 210</div>
      <div>Phoenix, AZ 85013</div>
    </div>
  </div>
</body>
</html>
```